Stationary Design for Stunning new Logo

I need to envelopes, letterhead, business cards designed to compliment our new logo.

We are a 25 year old printing company going through a brand refresh. All items should have the design extended to both sides for full print ability.

Industry/Entity Type

Printing

Requirements
Must have
• It must utilize the new logo & colors PMS 300 & PMS 295.

```html
<!DOCTYPE html>
<html lang="en">
<head>
<meta charset="utf-8">
<title>Inkvale Stationery Set</title>
<link href="https://fonts.googleapis.com/css2?family=Arimo:wght@400;700&display=swap" rel="stylesheet">
<style>
  :root {
    --navy: #0b2d62;
    --blue: #1a6fc9;
    --envelope: #28395c;
    --paper: #ffffff;
    --backdrop: #e9e6e1;
    --ink: #2a2a2a;
    --muted: #5a6272;
  }
  * { box-sizing: border-box; margin: 0; padding: 0; }
  html, body { width: 1200px; height: 1000px; overflow: hidden; }
  body { background: var(--backdrop); font-family: "Arimo", sans-serif; color: var(--ink); position: relative; }

  .piece { position: absolute; background: var(--paper); overflow: hidden; box-shadow: 2px 3px 6px rgba(0,0,0,.25); }
  .card { border-radius: 18px; }
  .card--dark { background: var(--navy); }
  .wave { position: absolute; left: 0; width: 100%; }

  .logo { position: absolute; display: flex; flex-direction: column; align-items: center; }
  .logo__row { display: flex; align-items: center; gap: .3em; }
  .logo__dot { width: .85em; height: .85em; border-radius: 50%; background: var(--blue); }
  .logo__name { font-weight: 700; color: var(--navy); letter-spacing: .02em; line-height: 1; }
  .logo__tag { font-size: .22em; color: var(--blue); text-transform: uppercase; margin-top: .25em; white-space: nowrap; }
  .logo--light .logo__name { color: #ffffff; }
  .logo--light .logo__dot { background: #ffffff; }
  .logo--light .logo__tag { color: #c9d6ea; }

  .person { position: absolute; text-align: right; }
  .person__name { font-weight: 700; font-size: 13px; line-height: 1.15; }
  .person__role { font-size: 11px; color: var(--blue); margin-bottom: 6px; line-height: 1.15; }
  .person__addr { font-size: 10.5px; line-height: 1.25; }
  .contacts { position: absolute; list-style: none; font-size: 10.5px; line-height: 1.3; padding-left: 8px; border-left: 1px solid currentColor; }
  .contacts li { display: flex; align-items: center; gap: 8px; }
  .ico { width: 9px; height: 9px; flex: none; }
  .on-dark { color: #ffffff; }
  .on-dark .person__role { color: #ffffff; }

  .url { position: absolute; width: 100%; text-align: center; color: #fff; font-size: 12px; }
  .footer-line { position: absolute; width: 100%; text-align: center; color: #fff; font-size: 6.5px; }
  .footer-contacts { position: absolute; width: 100%; display: flex; justify-content: center; gap: 18px; color: #fff; font-size: 6.5px; }
  .emblem { position: absolute; border-radius: 50%; }
</style>
</head>
<body>

<!-- Letterhead, centred header -->
<section class="piece letterhead" style="left:53px;top:41px;width:344px;height:446px">
  <div class="logo" style="left:0;width:100%;top:16px;font-size:20px">
    <div class="logo__row"><span class="logo__dot"></span><span class="logo__name">INKVALE</span></div>
    <div class="logo__tag">Reliable service • Crisp prints • Honest fair pricing</div>
  </div>
  <div class="emblem" style="left:72px;top:120px;width:200px;height:200px;background:#eef2f8"></div>
  <svg class="wave" style="top:390px;height:56px" viewBox="0 0 344 56" preserveAspectRatio="none">
    <path d="M0,6 C90,-2 220,22 344,16 L344,56 L0,56 Z" fill="var(--blue)"/>
    <path d="M0,14 C90,6 220,28 344,21 L344,56 L0,56 Z" fill="#fff"/>
    <path d="M0,17 C90,10 220,30 344,24 L344,56 L0,56 Z" fill="var(--navy)"/>
  </svg>
  <p class="footer-line" style="top:421px">412, "Sagar" Complex, Neel park Soc., Vora road, Surat-395001</p>
  <div class="footer-contacts" style="top:431px">
    <span>+91 222 3334444</span><span>+91 222 3334444</span><span>name@email.com</span><span>www.inkvale.com</span>
  </div>
</section>

<!-- Business card front, dark lower half -->
<section class="piece card" style="left:469px;top:90px;width:330px;height:188px">
  <div class="logo" style="left:0;width:100%;top:26px;font-size:22px">
    <div class="logo__row"><span class="logo__dot"></span><span class="logo__name">INKVALE</span></div>
    <div class="logo__tag">Reliable service • Crisp prints • Honest fair pricing</div>
  </div>
  <svg class="wave" style="top:76px;height:112px" viewBox="0 0 330 112" preserveAspectRatio="none">
    <path d="M0,8 C100,-6 220,30 330,6 L330,112 L0,112 Z" fill="var(--blue)"/>
    <path d="M0,16 C100,4 220,36 330,14 L330,112 L0,112 Z" fill="#fff"/>
    <path d="M0,20 C100,8 220,40 330,18 L330,112 L0,112 Z" fill="var(--navy)"/>
  </svg>
  <div class="person on-dark" style="right:172px;top:112px;width:150px">
    <p class="person__name">Name Surname</p>
    <p class="person__role">Designation</p>
    <p class="person__addr">412, "Sagar" complex,<br>Neel park soc., Vora<br>road, Surat - 395007</p>
  </div>
  <ul class="contacts on-dark" style="left:168px;top:116px">
    <li><svg class="ico" viewBox="0 0 10 10"><path d="M2,0 L4,2 L3,4 Q5,6 6,7 L8,6 L10,8 L8,10 Q0,8 0,2 Z" fill="#fff"/></svg>+91 222 3334444</li>
    <li><svg class="ico" viewBox="0 0 10 10"><rect x="1" y="3" width="8" height="6" fill="#fff"/><rect x="3" y="0" width="4" height="3" fill="#fff"/></svg>+91 222 3334444</li>
    <li><svg class="ico" viewBox="0 0 10 10"><rect x="0" y="2" width="10" height="7" fill="#fff"/><path d="M0,2 L5,6 L10,2" stroke="var(--navy)" fill="none"/></svg>name@email.com</li>
    <li><svg class="ico" viewBox="0 0 10 10"><circle cx="5" cy="5" r="4.5" fill="#fff"/></svg>www.inkvale.com</li>
  </ul>
</section>

<!-- Business card front, white with wave at foot -->
<section class="piece card" style="left:807px;top:90px;width:331px;height:188px">
  <div class="logo" style="left:0;width:100%;top:14px;font-size:22px">
    <div class="logo__row"><span class="logo__dot"></span><span class="logo__name">INKVALE</span></div>
    <div class="logo__tag">Reliable service • Crisp prints • Honest fair pricing</div>
  </div>
  <div class="person" style="right:172px;top:61px;width:150px">
    <p class="person__name">Name Surname</p>
    <p class="person__role">Designation</p>
    <p class="person__addr">412, "Sagar" complex,<br>Neel park soc., Vora<br>road, Surat - 395007</p>
  </div>
  <ul class="contacts" style="left:168px;top:66px;color:var(--ink)">
    <li><svg class="ico" viewBox="0 0 10 10"><path d="M2,0 L4,2 L3,4 Q5,6 6,7 L8,6 L10,8 L8,10 Q0,8 0,2 Z" fill="var(--navy)"/></svg>+91 222 3334444</li>
    <li><svg class="ico" viewBox="0 0 10 10"><rect x="1" y="3" width="8" height="6" fill="var(--navy)"/><rect x="3" y="0" width="4" height="3" fill="var(--navy)"/></svg>+91 222 3334444</li>
    <li><svg class="ico" viewBox="0 0 10 10"><rect x="0" y="2" width="10" height="7" fill="var(--navy)"/><path d="M0,2 L5,6 L10,2" stroke="#fff" fill="none"/></svg>name@email.com</li>
    <li><svg class="ico" viewBox="0 0 10 10"><circle cx="5" cy="5" r="4.5" fill="var(--navy)"/></svg>www.inkvale.com</li>
  </ul>
  <svg class="wave" style="top:138px;height:50px" viewBox="0 0 331 50" preserveAspectRatio="none">
    <path d="M0,10 C110,28 230,-6 331,8 L331,50 L0,50 Z" fill="var(--blue)"/>
    <path d="M0,18 C110,34 230,2 331,16 L331,50 L0,50 Z" fill="#fff"/>
    <path d="M0,21 C110,37 230,5 331,19 L331,50 L0,50 Z" fill="var(--navy)"/>
  </svg>
</section>

<!-- Business card back, emblem -->
<section class="piece card card--dark" style="left:469px;top:294px;width:331px;height:190px">
  <div class="emblem" style="left:118px;top:42px;width:96px;height:96px;background:#ffffff"></div>
  <p class="url" style="top:152px">www.inkvale.com</p>
</section>

<!-- Business card back, name -->
<section class="piece card card--dark" style="left:807px;top:296px;width:331px;height:190px">
  <div class="logo logo--light" style="left:0;width:100%;top:80px;font-size:22px">
    <div class="logo__row"><span class="logo__dot"></span><span class="logo__name">INKVALE</span></div>
    <div class="logo__tag">Reliable service • Crisp prints • Honest fair pricing</div>
  </div>
  <p class="url" style="top:154px">www.inkvale.com</p>
</section>

<!-- Letterhead, side header -->
<section class="piece letterhead" style="left:53px;top:517px;width:344px;height:446px">
  <div class="logo" style="left:12px;top:26px;font-size:19px;align-items:flex-start">
    <div class="logo__row"><span class="logo__dot"></span><span class="logo__name">INKVALE</span></div>
    <div class="logo__tag">Reliable service • Crisp prints • Honest fair pricing</div>
  </div>
  <p class="person__addr" style="position:absolute;right:90px;top:24px;font-size:7px;text-align:right">412, "Sagar" complex,<br>Neel park soc., Vora<br>road, Surat - 395007</p>
  <ul class="contacts" style="left:258px;top:20px;font-size:7px;color:var(--ink)">
    <li>+91 222 3334444</li><li>+91 222 3334444</li><li>name@email.com</li><li>www.inkvale.com</li>
  </ul>
  <div class="emblem" style="left:72px;top:120px;width:200px;height:200px;background:#eef2f8"></div>
  <svg class="wave" style="top:400px;height:46px" viewBox="0 0 344 46" preserveAspectRatio="none">
    <path d="M0,6 C90,-2 220,20 344,14 L344,46 L0,46 Z" fill="var(--blue)"/>
    <path d="M0,13 C90,6 220,26 344,20 L344,46 L0,46 Z" fill="#fff"/>
    <path d="M0,16 C90,9 220,29 344,23 L344,46 L0,46 Z" fill="var(--navy)"/>
  </svg>
  <p class="footer-line" style="top:431px;font-weight:700">www.inkvale.com</p>
</section>

<!-- Compliment slip -->
<section class="piece slip" style="left:469px;top:554px;width:428px;height:186px">
  <div class="logo" style="left:12px;top:12px;font-size:12px;align-items:flex-start">
    <div class="logo__row"><span class="logo__dot"></span><span class="logo__name">INKVALE</span></div>
    <div class="logo__tag">Reliable service • Crisp prints • Honest fair pricing</div>
  </div>
  <div class="emblem" style="left:282px;top:28px;width:110px;height:110px;background:#eef2f8"></div>
  <svg class="wave" style="top:138px;height:48px" viewBox="0 0 428 48" preserveAspectRatio="none">
    <path d="M0,10 C110,26 300,-6 428,8 L428,48 L0,48 Z" fill="var(--blue)"/>
    <path d="M0,18 C110,32 300,2 428,15 L428,48 L0,48 Z" fill="#fff"/>
    <path d="M0,21 C110,35 300,5 428,18 L428,48 L0,48 Z" fill="var(--navy)"/>
  </svg>
  <p class="footer-line" style="top:169px;text-align:right;padding-right:12px;font-size:7px">412, "Sagar" Complex, Neel park Soc., Vora road, Surat-395001</p>
</section>

<!-- Envelope back -->
<section class="piece envelope" style="left:708px;top:772px;width:430px;height:190px;background:var(--envelope)">
  <svg class="wave" style="top:0;height:80px" viewBox="0 0 430 80" preserveAspectRatio="none">
    <path d="M0,0 L180,62 Q215,74 250,62 L430,0" fill="none" stroke="rgba(0,0,0,.25)" stroke-width="2"/>
  </svg>
  <div class="logo logo--light" style="left:0;width:100%;top:20px;font-size:17px">
    <div class="logo__row"><span class="logo__dot"></span><span class="logo__name">INKVALE</span></div>
    <div class="logo__tag">Reliable service • Crisp prints • Honest fair pricing</div>
  </div>
  <div class="emblem" style="left:296px;top:58px;width:110px;height:110px;background:rgba(0,0,0,.12)"></div>
</section>

</body>
</html>
```